New Phone Case requires logo and packaging

We need a nice and sleek logo designed along with packaging for our Premium Phone Case brand

Our Brand Name is Vaxel
Please note this has nothing to do with a Rhino so don't put a Rhino in the logo
I've also attached a file called VAXEL Logo Inspiration, which shows something along the lines of the type of text we want to use. Please note i have photoshopped that image together from another logo we had, and i liked the text, but its for you to see what direction we want to go in. Also note i have shown different variations in that image file, use your imagination with it and show us a nice and clean logo.

We would like the Brand in upper caps such as VAXEL
The brand is for Premium Phone Cases. The first thing that should come to someones mind when looking at the branding is High Quality, Premium and Modern.

The look must be high end and modern

The design must portray high quality and premium!

Also i will say "Less is More". Don't cramp many things on the packaging and logo. We just want a nice, clean cut high quality logo and packaging

I have attached images of an example packaging from a few competitors. One is a standard open from top packaging, while another is a slide out packaging. Our packaging dimensions should be the same which are Packaging dimensions
Length = 18cm
Height = 1.5cm
Depth = 9.5cm

Also note the example packaging has a transparent front section to show which case is inside, this is optional if you want to have it. If not you can cover it all up.

Font styles to use
Other font styles liked:
• Any nice font but just not the standard everyday stuff like Arial, San Serif etc as i want it to be differentiated. A Font that shows Serious Quality and one that stands out would be awesome!

Colors

Designer to choose colors to be used in the design.

Requirements
Must have
• Must be a nice and clean design
• Packaging dimensions
• Length = 18cm
• Height = 1.5cm
• Depth = 9.5cm

```html
<!DOCTYPE html>
<html lang="en">
<head>
<meta charset="utf-8">
<title>Vaxel Packaging – Front and Back Panels</title>
<link rel="stylesheet" href="https://fonts.googleapis.com/css2?family=Montserrat:wght@400;500;700&display=swap">
<style>
  :root {
    --bg: #141414;
    --gold: #f0ad3c;
    --window: #3a3a3a;
  }
  html, body {
    margin: 0;
    padding: 0;
    width: 1200px;
    height: 1200px;
    overflow: hidden;
    background: var(--bg);
  }
  .canvas {
    display: block;
    width: 1200px;
    height: 1200px;
  }
  .accent-bar { fill: var(--gold); }
  .rule { stroke: var(--gold); stroke-width: 1.4; }
  .product-window { fill: var(--window); }
  .wordmark {
    font-family: "Montserrat", sans-serif;
    font-weight: 700;
    font-size: 66px;
    letter-spacing: 4px;
    fill: var(--gold);
  }
  .tagline {
    font-family: "Montserrat", sans-serif;
    font-weight: 500;
    font-size: 15px;
    letter-spacing: 5px;
    fill: var(--gold);
  }
  .headline {
    font-family: "Montserrat", sans-serif;
    font-weight: 500;
    font-size: 20px;
    letter-spacing: 6px;
    fill: var(--gold);
  }
  .feature-label {
    font-family: "Montserrat", sans-serif;
    font-weight: 500;
    font-size: 9px;
    letter-spacing: 1px;
    fill: var(--gold);
  }
  .feature-copy {
    font-family: "Montserrat", sans-serif;
    font-weight: 400;
    font-size: 9px;
    fill: var(--gold);
  }
  .web-address {
    font-family: "Montserrat", sans-serif;
    font-weight: 500;
    font-size: 13px;
    letter-spacing: 6px;
    fill: var(--gold);
  }
</style>
</head>
<body>
<svg class="canvas" viewBox="0 0 1200 1200" xmlns="http://www.w3.org/2000/svg">
  <!-- Front panel -->
  <g class="panel-front">
    <rect class="accent-bar" x="339" y="245" width="11" height="160"/>
    <text class="wordmark" x="300" y="471" text-anchor="middle">VAXEL</text>
    <line class="rule" x1="170" y1="489" x2="430" y2="489"/>
    <text class="tagline" x="302" y="513" text-anchor="middle">LESS IS MORE</text>
    <line class="rule" x1="170" y1="525" x2="430" y2="525"/>
    <rect class="accent-bar" x="339" y="534" width="11" height="202"/>
    <rect class="product-window" x="139" y="773" width="323" height="94" rx="47"/>
    <rect class="accent-bar" x="339" y="890" width="11" height="70"/>
  </g>

  <!-- Back panel -->
  <g class="panel-back">
    <rect class="accent-bar" x="935" y="245" width="11" height="154"/>
    <line class="rule" x1="744" y1="401" x2="1052" y2="401"/>
    <text class="headline" x="900" y="439" text-anchor="middle">BEST PROTECTION</text>
    <text class="feature-label" x="900" y="461" text-anchor="middle">PERFECT FIT</text>
    <line class="rule" x1="795" y1="469" x2="1004" y2="469"/>
    <text class="feature-copy" x="900" y="480" text-anchor="middle">Slim shockproof shell with raised edge protection</text>
    <text class="feature-copy" x="900" y="491" text-anchor="middle">Precision cutouts for buttons, ports and camera</text>
    <text class="feature-copy" x="900" y="502" text-anchor="middle">Soft microfiber lining keeps your phone scratch free</text>
    <line class="rule" x1="744" y1="516" x2="1052" y2="516"/>
    <rect class="accent-bar" x="935" y="520" width="11" height="216"/>
    <line class="rule" x1="755" y1="738" x2="1026" y2="738"/>
    <text class="web-address" x="900" y="779" text-anchor="middle">www.vaxel.com</text>
    <line class="rule" x1="755" y1="808" x2="1026" y2="808"/>
  </g>
</svg>
</body>
</html>
```